Business Card Design

Hoping for a black background business card, minimalistic design.
With the Marble Crest logo you created in white.

I would like to include:
My Name and title
Address (street address)
Reception: (phone number)
Fax: (fax number)
Reception: (email address)
Direct email: (email address)
Instagram: (ig handle)

```html
<!DOCTYPE html>
<html lang="en">
<head>
<meta charset="utf-8">
<title>Marble Crest — Business Card</title>
<link rel="stylesheet" href="https://fonts.googleapis.com/css2?family=Montserrat:wght@300;400;500;700&display=swap">
<style>
  :root {
    --canvas-bg: #ececec;
    --card-black: #0d0d0d;
    --card-pattern-a: #121212;
    --card-pattern-b: #1c1c1c;
    --card-white: #ffffff;
    --ink-light: #ffffff;
    --ink-muted: #cfcfcf;
    --ink-dark: #1a1a1a;
    --rule: #5a5a5a;
  }
  * { margin: 0; padding: 0; box-sizing: border-box; }
  html, body { width: 1200px; height: 1200px; overflow: hidden; }
  body {
    background: var(--canvas-bg);
    font-family: "Montserrat", Arial, sans-serif;
    display: flex;
    flex-direction: column;
    align-items: center;
    justify-content: center;
    gap: 56px;
  }
  .card {
    position: relative;
    width: 900px;
    height: 514px;
    overflow: hidden;
    box-shadow: 0 18px 40px rgba(0,0,0,0.18);
  }
  .card--front { background: var(--card-black); color: var(--ink-light); }
  .card--back { background: var(--card-white); color: var(--ink-dark); }

  .card__pattern {
    position: absolute;
    inset: 0;
    background: radial-gradient(ellipse at 30% 40%, var(--card-pattern-b), var(--card-pattern-a) 70%);
  }

  .brand {
    position: absolute;
    display: flex;
    align-items: center;
    gap: 16px;
    white-space: nowrap;
  }
  .brand__dot {
    flex-shrink: 0;
    border-radius: 50%;
    border: 3px solid currentColor;
  }
  .brand__name {
    font-weight: 500;
    letter-spacing: 0.08em;
    text-transform: uppercase;
  }
  .card--front .brand { left: 76px; top: 326px; }
  .card--front .brand__dot { width: 60px; height: 60px; }
  .card--front .brand__name { font-size: 24px; }

  .card--back .brand { left: 50%; top: 50%; transform: translate(-50%, -50%); }
  .card--back .brand__dot { width: 70px; height: 70px; }
  .card--back .brand__name { font-size: 28px; }

  .contact {
    position: absolute;
    left: 480px;
    top: 160px;
    width: 380px;
  }
  .contact__name {
    font-size: 35px;
    font-weight: 700;
    letter-spacing: 0.02em;
    line-height: 1;
    white-space: nowrap;
  }
  .contact__title {
    font-size: 20px;
    font-weight: 300;
    color: var(--ink-muted);
    margin-top: 6px;
    white-space: nowrap;
  }
  .contact__group {
    margin-top: 24px;
    padding-bottom: 9px;
    border-bottom: 1px solid var(--rule);
  }
  .contact__group + .contact__group { margin-top: 10px; }
  .contact__group--last { border-bottom: none; padding-bottom: 0; }
  .contact__row {
    display: flex;
    align-items: baseline;
    line-height: 1.5;
  }
  .contact__label {
    flex: 0 0 130px;
    font-size: 11px;
    font-weight: 500;
    letter-spacing: 0.06em;
    text-transform: uppercase;
  }
  .contact__value {
    font-size: 16px;
    font-weight: 400;
    color: var(--ink-muted);
    white-space: nowrap;
  }
</style>
</head>
<body>
  <section class="card card--front">
    <div class="card__pattern" role="img" aria-label="Faint tonal repeating emblem pattern across the black card"></div>

    <div class="brand">
      <span class="brand__dot"></span>
      <span class="brand__name">Marble Crest</span>
    </div>

    <div class="contact">
      <h1 class="contact__name">DANIEL REYES</h1>
      <p class="contact__title">Marketing Director</p>

      <div class="contact__group">
        <div class="contact__row"><span class="contact__label">Reception</span><span class="contact__value">(+000)123-4567</span></div>
        <div class="contact__row"><span class="contact__label">Fax</span><span class="contact__value">(+000)123-4567</span></div>
      </div>

      <div class="contact__group">
        <div class="contact__row"><span class="contact__label">Direct</span><span class="contact__value">yourgmail@name.com</span></div>
        <div class="contact__row"><span class="contact__label">Reception</span><span class="contact__value">yourgmail@name.com</span></div>
      </div>

      <div class="contact__group contact__group--last">
        <div class="contact__row"><span class="contact__label">Address</span><span class="contact__value">123 Street Name City</span></div>
        <div class="contact__row"><span class="contact__label"></span><span class="contact__value">Name State, Country, 12345</span></div>
      </div>
    </div>
  </section>

  <section class="card card--back">
    <div class="brand">
      <span class="brand__dot"></span>
      <span class="brand__name">Marble Crest</span>
    </div>
  </section>
</body>
</html>
```